Medical Internet Marketing Company Needs a Site!

We need a new, fresh website for our search engine optimization and social media marketing company. We specialize in helping medical practices, doctors, physicians, and hospitals with their online presence and web ranking. The site should lean towards being suited for these audiences.

We have several examples of website that we like as well as things that we like about them.

Here are sites that we enjoy.

www.brightwavelab.com

It's a good design for the site all around. The videos, buttons, and images are all excellent. They did a fine job.

- We really like their "contact us" side bar and want to include one like it on the secondary pages.

www.corvantis.net

- We don't like the "thickness" of the top navigation bar.
- We like the page colors, easy navigation, and big call to action phone number in the top right corner.

http://www.teluvo.com/

Out of all the examples provided, Teluvo is our favorite and closest look and style to what we are looking for.

- We really like the openness of the design, such as space between the text and background.

- We want a price page in a style very similar to their pricing page with the services listed and check-marks, etc. although we intend to have multiple service package columns much like Corvantis's SEO pricing page.

- The way the video fits into the home page header is very organized, simple, and attention grabbing. We intend to place a slider with videos here.

- We need a page design that will allow for an image slider like Teluvo's Features page.

Here's a great example of a medical internet marketing website: http://www.dermaplex.com/

Target Market(s)

Our target market is doctors, typically male and typically 40-45 years old. I

Industry/Entity Type

Marketing

Requirements
Must have
• The homepage should have a slider in the video. Interior pages should have a video in the very top similar to how they do it on www.brightwavelab.com

The top navigation tabs needed are:
- Home
- Solutions
- Resources
- About
- Why Quelvo
- Contact

The sidebar should have a GREAT call to action in it on interior pages.

There should be one interior page that is similar to this - http://www.teluvo.com/pricing/

There needs to be a page with multiple boxes that take up a row of the web page's body. This page will house all the case studies similar to brightwave lab's: http://www.brightwavelab.com/success-stories/case-studies/ The one exception is we want the case studies to be inside of "boxes" instead of between horizontal lines like brightwave lab's.
Nice to have
• Color, professional, and clean. GREAT use of calls to actions.

```html
<!DOCTYPE html>
<html lang="en">
<head>
<meta charset="utf-8">
<title>Quelvo — Internet Marketing for Medical Practices</title>
<link href="https://fonts.googleapis.com/css2?family=Arimo:wght@400;700&family=Cabin:wght@400;500&family=Gelasio:wght@400&display=swap" rel="stylesheet">
<style>
:root{
  --page:#f1f1f1;
  --ink:#333;
  --ink-soft:#555;
  --muted:#888;
  --orange:#f4a460;
  --teal:#5ec8b8;
  --sky:#8fd6ef;
  --lime:#8cc63f;
  --dark:#2b2b2b;
  --footer:#a7a7a9;
  --line:#dcdcdc;
  --serif:'Gelasio', Georgia, serif;
  --sans:'Arimo', Arial, sans-serif;
  --hero:'Cabin', Arial, sans-serif;
}
*{margin:0;padding:0;box-sizing:border-box}
html,body{width:960px;height:1200px;overflow:hidden;background:#fff}
.page{position:absolute;left:34px;top:0;width:892px;height:1198px;background:var(--page);overflow:hidden;font-family:var(--sans);color:var(--ink)}
.abs{position:absolute}
.backdrop{position:absolute;left:0;top:0}
/* header */
.callout{left:574px;top:14px;font-size:8px;color:var(--muted);display:flex;align-items:center;gap:4px}
.callout .num{font-family:var(--serif);font-size:15px;color:var(--orange)}
.brand{left:123px;top:53px;display:flex;align-items:center;gap:8px}
.brand .mark{width:18px;height:18px;background:var(--teal)}
.brand .word{font-family:var(--sans);font-size:27px;letter-spacing:3px;color:#7a7a7a;line-height:1}
.nav{left:358px;top:53px;width:414px;height:26px;background:#fff;border-radius:13px;box-shadow:0 2px 4px rgba(0,0,0,.12);display:flex;overflow:hidden}
.nav a{flex:1;font-family:var(--serif);font-size:10px;color:#888;text-decoration:none;display:flex;align-items:center;justify-content:center;border-left:1px solid #e6e6e6}
.nav a:first-child{border-left:none;background:linear-gradient(#8ddcd0,#5cc4b4);color:#fff}
/* hero */
.hero{left:123px;top:122px;width:646px;height:229px;box-shadow:0 1px 3px rgba(0,0,0,.15)}
.hero-quote{position:absolute;left:0;top:0;width:339px;height:229px;background:linear-gradient(180deg,var(--sky),var(--teal));color:#fff;font-family:var(--hero)}
.hero-quote h2{position:absolute;left:22px;top:48px;font-weight:400;font-size:18px;white-space:nowrap}
.hero-quote p{position:absolute;left:22px;top:78px;width:296px;font-size:11.4px;line-height:15.6px;color:#1f3a3a}
.hero-quote .who{position:absolute;left:23px;top:144px;font-size:15px;line-height:20px}
.hero-quote .who b{display:block;font-weight:400;color:#1f3a3a}
.hero-next{position:absolute;left:323px;top:98px;width:17px;height:34px;background:#fff;border-radius:17px 0 0 17px}
.hero-next:after{content:"";position:absolute;left:7px;top:12px;border-left:6px solid var(--orange);border-top:5px solid transparent;border-bottom:5px solid transparent}
.hero-video{position:absolute;left:339px;top:0;width:307px;height:229px;background:radial-gradient(ellipse 40% 60% at 60% 60%,#e9ece6,#a7d46a 70%,#7ab830)}
.player{position:absolute;left:9px;top:204px;width:285px;height:20px;display:flex;gap:2px}
.player .play{width:46px;height:20px;background:var(--dark);border-radius:3px;position:relative}
.player .play:after{content:"";position:absolute;left:19px;top:5px;border-left:9px solid #fff;border-top:5px solid transparent;border-bottom:5px solid transparent}
.player .bar{flex:1;background:var(--dark);border-radius:3px;position:relative}
.player .track{position:absolute;left:8px;top:8px;width:138px;height:5px;border:1px solid #777}
.player .time{position:absolute;left:-7px;top:-6px;background:#fff;color:#222;font-size:7px;padding:0 2px}
.player .vol{position:absolute;left:154px;top:7px;width:22px;height:7px;background:repeating-linear-gradient(90deg,#4aa8d8 0 2px,transparent 2px 3px)}
.player .host{position:absolute;right:8px;top:3px;color:#fff;font-size:11px;font-weight:700;font-family:var(--sans)}
/* service boxes */
.pillar{top:374px;width:214px;height:100px;background:linear-gradient(#fff,#ebebeb);border:1px solid #ddd;box-shadow:0 1px 2px rgba(0,0,0,.08);text-align:center}
.pillar .art{width:54px;height:52px;margin:9px auto 0;border-radius:50%}
.pillar h3{font-family:var(--serif);font-weight:400;font-size:14.5px;color:#444;margin-top:12px}
/* sections */
.section-title{font-family:var(--serif);font-weight:400;font-size:19px;color:#333;white-space:nowrap}
.points{left:120px;top:536px;display:flex;font-size:9px;color:#555;white-space:nowrap}
.points span{display:flex;align-items:center;gap:6px;margin-right:23px}
.points i{width:6px;height:6px;border-radius:50%;display:inline-block}
.rule{left:120px;width:648px;height:0;border-top:1px dotted var(--line)}
.service{width:210px;height:56px}
.service .thumb{position:absolute;left:0;top:0;width:61px;height:55px;background:#fff;border:1px solid #ddd;box-shadow:0 1px 2px rgba(0,0,0,.1);padding:5px}
.service .thumb div{width:100%;height:100%}
.service h4{position:absolute;left:70px;top:0;font-weight:400;font-size:10px;color:#333;white-space:nowrap}
.service p{position:absolute;left:70px;top:18px;width:136px;font-size:8px;line-height:10px;color:#555}
.about{left:120px;top:873px;width:640px;font-size:8px;line-height:12px;color:#555}
/* social band */
.social{left:0;top:941px;width:892px;height:53px;background:linear-gradient(#fff,#ececec)}
.social h3{position:absolute;left:118px;top:14px;font-family:var(--serif);font-weight:400;font-size:19px;color:#333}
.social .links{position:absolute;left:260px;top:15px;display:flex;gap:3px}
.social .links span{width:26px;height:26px;background:#6a6a6a;border-radius:2px}
/* footer */
.footer{left:0;top:994px;width:892px;height:204px;background:var(--footer);color:#fff}
.footer h3{position:absolute;left:120px;top:21px;font-family:var(--serif);font-weight:400;font-size:12px}
.markets{position:absolute;left:121px;top:52px;font-size:8px;line-height:15px;letter-spacing:.2px}
.markets ul{position:absolute;top:0;list-style:none;white-space:nowrap}
.footer .rule{border-top-color:#c3c3c5;top:133px}
.footer small{position:absolute;left:120px;top:161px;font-size:7px}
.footer .brand{left:604px;top:155px}
.footer .brand .mark{background:#5f5f61;width:16px;height:16px}
.footer .brand .word{color:#5f5f61;font-size:22px}
</style>
</head>
<body>
<div class="page">
  <svg class="backdrop" width="892" height="941" viewBox="0 0 892 941" aria-hidden="true">
    <polygon points="0,0 330,0 0,600" fill="#dfe9cf" opacity=".7"/>
    <polygon points="0,120 250,520 0,940" fill="#b8dba8" opacity=".7"/>
    <polygon points="120,470 330,470 470,940 300,940" fill="#bfe0f2" opacity=".75"/>
    <polygon points="330,470 560,820 470,940" fill="#a9d6ee" opacity=".6"/>
    <polygon points="0,600 220,940 0,940" fill="#d7e7c6" opacity=".8"/>
    <polygon points="600,0 892,0 892,420" fill="#e4e4e4" opacity=".7"/>
  </svg>

  <div class="abs callout">
    <svg width="24" height="18" viewBox="0 0 24 18" aria-hidden="true"><path d="M4 2c-3 3-2 8 4 12 5 3 9 3 11 1l-3-4-3 2c-2-1-4-3-5-5l2-3z" fill="#3a8ad6"/></svg>
    Call Us Today: <span class="num">(555-014-2837)</span>
  </div>
  <div class="abs brand"><span class="mark"></span><span class="word">QUELVO</span></div>
  <nav class="abs nav">
    <a href="#">Home</a><a href="#">Solutions</a><a href="#">Resources</a><a href="#">About</a><a href="#">Why Quelvo</a><a href="#">Contact</a>
  </nav>

  <section class="abs hero">
    <div class="hero-quote">
      <h2>SEO / Internet Marketing / Consulting</h2>
      <p>Quelvo has been a great resource for Hollis Media Group. We ’ve developed an incredible relationship with them, and it’s awesome to have an SEO company we can partner with.</p>
      <div class="who">Dana Hollis<b>Hollis Media Group</b></div>
      <span class="hero-next"></span>
    </div>
    <div class="hero-video" role="img" aria-label="Video still of a doctor in a white coat with stethoscope, arms crossed, on a green dotted backdrop">
      <div class="player">
        <span class="play"></span>
        <span class="bar"><span class="time">02:47</span><span class="track"></span><span class="vol"></span><span class="host">vidora</span></span>
      </div>
    </div>
  </section>

  <div class="abs pillar" style="left:120px"><div class="art" role="img" aria-label="Globe with circular orange and blue arrows" style="background:radial-gradient(circle,#f39c3a,#3a8ad6)"></div><h3>Search Engine Optimization</h3></div>
  <div class="abs pillar" style="left:339px"><div class="art" role="img" aria-label="Blue globe with a network cable" style="background:radial-gradient(circle,#cfe6fa,#3a7fc8)"></div><h3>Internet Marketing</h3></div>
  <div class="abs pillar" style="left:558px"><div class="art" role="img" aria-label="Two business people in consultation" style="border-radius:8px;background:linear-gradient(#7a4a2a,#222 60%,#b02020)"></div><h3>Consulting</h3></div>

  <h2 class="abs section-title" style="left:120px;top:497px">Internet Marketing &amp; Websites for Medical Practices</h2>
  <div class="abs points">
    <span><i style="background:var(--teal)"></i>Proven to help grow medical practices — 6,000+ satisfied clients</span>
    <span><i style="background:var(--lime)"></i>Websites, mobile sites, local search and more...</span>
    <span><i style="background:var(--orange)"></i>Fast, easy and affordable</span>
  </div>
  <div class="abs rule" style="top:564px"></div>

  <h2 class="abs section-title" style="left:120px;top:584px">Medical Website Services</h2>

  <div class="abs service" style="left:121px;top:626px">
    <div class="thumb"><div role="img" aria-label="Desktop computer monitor" style="background:linear-gradient(#3a6fb0,#c9c9c9)"></div></div>
    <h4>WEBSITES</h4>
    <p>Your site will be fully customized to showcase your practice. We take care of all the backend technology so that you can stay focused on your work...</p>
  </div>
  <div class="abs service" style="left:346px;top:626px">
    <div class="thumb"><div role="img" aria-label="Smartphone" style="background:linear-gradient(90deg,#fff 30%,#333 30% 70%,#fff 70%)"></div></div>
    <h4>MOBILE WEBSITES</h4>
    <p>WE offers a mobile website feature that allows you to connect with new and existing patients anywhere, any time...</p>
  </div>
  <div class="abs service" style="left:569px;top:626px">
    <div class="thumb"><div role="img" aria-label="Search engine wordmark" style="background:#f6f6f6"></div></div>
    <h4>LOCAL SEARCH MARKETING</h4>
    <p>When people are looking for medical assistance, they go to one place: the Internet...</p>
  </div>
  <div class="abs service" style="left:121px;top:728px">
    <div class="thumb"><div role="img" aria-label="Blue and orange speech bubbles" style="background:linear-gradient(135deg,#3a9ae0 50%,#f5b335 50%);border-radius:40%"></div></div>
    <h4>MAPS &amp; REVIEWS</h4>
    <p>Dermaplex will launch your local directory presence in the top review sites, and use an array of online and offline programs to protect ...</p>
  </div>
  <div class="abs service" style="left:346px;top:728px">
    <div class="thumb"><div role="img" aria-label="Stack of colourful books" style="background:linear-gradient(90deg,#c0392b 33%,#2e6fb0 33% 66%,#2a9d8f 66%)"></div></div>
    <h4>PATIENT EDUCATION</h4>
    <p>Education is the key to preventative healthcare and treatment acceptance.</p>
  </div>
  <div class="abs service" style="left:569px;top:728px">
    <div class="thumb"><div role="img" aria-label="Cartoon doctor figure" style="background:linear-gradient(#e0b080 40%,#3a7fc8 40%);border-radius:6px"></div></div>
    <h4>PRACTICE HUB</h4>
    <p>Our exclusive Web presence management tool, Practice Hub, allows you to easily manage your entire online presence...</p>
  </div>

  <div class="abs rule" style="top:820px"></div>
  <h2 class="abs section-title" style="left:120px;top:840px">Medical Websites that Deliver Patients and Referrals</h2>
  <p class="abs about">Dermaplex is the world's leading provider of websites and online marketing for healthcare practices. We are recommended by more than 20 highly regarded medical associations and have worked with over 6,000 healthcare providers worldwide. Our medical practice website services can give you top rankings on Searchly, a strong image for your practice, more patients and more referrals.</p>

  <section class="abs social">
    <h3>Let’s Be Social!</h3>
    <div class="links" aria-label="Social profiles"><span></span><span></span><span></span><span></span></div>
  </section>

  <footer class="abs footer">
    <h3>Medical Markets:</h3>
    <div class="markets">
      <ul style="left:0"><li>Medical</li><li>Dental</li><li>Cosmetic Dental</li></ul>
      <ul style="left:99px"><li>Endodontic</li><li>Orthodontic</li><li>Pediatric Dental</li></ul>
      <ul style="left:198px"><li>Physician/Doctor</li><li>Audiology</li><li>Cardiology</li></ul>
      <ul style="left:299px"><li>Chiropractic</li><li>Dermatology</li><li>ENT</li></ul>
      <ul style="left:391px"><li>Gastroenterology</li><li>Midwifery</li><li>OB-GYN</li></ul>
      <ul style="left:498px"><li>Otolaryngology</li><li>Pediatric</li><li>Physical Therapy</li></ul>
      <ul style="left:611px"><li>Podiatry</li><li>Urology</li><li>Veterinary</li></ul>
    </div>
    <div class="abs rule"></div>
    <small>© 2012 QUELVO.COM. All Rights Reserved.</small>
    <div class="abs brand"><span class="mark"></span><span class="word">QUELVO</span></div>
  </footer>
</div>
</body>
</html>
```